Business Card Design Project

I am an aviation professional (corporate pilot), and am looking to market myself to the business jet operators for short term crew leasing. The card should have name and contact info on the front side; qualifications, licenses held and type ratings on the back side.
Company name is: Skyvale Roster Partners Inc.
Updates

Sorry for the delay. will reply in another day or two.
best regards,

P

Target Market(s)

Business Jet Management companies and private jet operators

Industry/Entity Type

Business

Requirements
Must have
• It needs to be an aviation inspired design.

```html
<!DOCTYPE html>
<html lang="en">
<head>
<meta charset="utf-8">
<title>Skyvale Roster Partners Inc. – Business Card</title>
<link rel="stylesheet" href="https://fonts.googleapis.com/css2?family=Questrial&family=Open+Sans:ital,wght@0,400;0,700;1,400&display=swap">
<style>
  :root {
    --backdrop: #ececec;
    --card: #ffffff;
    --ink: #676767;
    --ink-soft: #777777;
    --accent: #d8161e;
    --sweep-light: #f6f6f6;
    --sweep-dark: #c6c6c6;
  }
  * { margin: 0; padding: 0; box-sizing: border-box; }
  html, body {
    width: 1200px;
    height: 900px;
    overflow: hidden;
    background: var(--backdrop);
  }
  .canvas {
    position: relative;
    width: 1200px;
    height: 900px;
  }
  .card {
    position: absolute;
    left: 246px;
    top: 242px;
    width: 708px;
    height: 416px;
    background: var(--card);
    overflow: hidden;
  }
  .card__sweep {
    position: absolute;
    inset: 0;
    width: 708px;
    height: 416px;
  }
  .brand {
    position: absolute;
    left: 40px;
    top: 86px;
    display: flex;
    align-items: center;
    gap: 12px;
  }
  .brand__dot {
    width: 18px;
    height: 18px;
    border-radius: 50%;
    background: var(--accent);
    flex: none;
  }
  .brand__name {
    font-family: "Questrial", sans-serif;
    font-size: 25px;
    line-height: 30px;
    color: var(--ink);
  }
  .holder {
    position: absolute;
    left: 0;
    width: 708px;
    top: 206px;
    text-align: center;
    font-family: "Open Sans", sans-serif;
  }
  .holder__name {
    font-weight: 700;
    font-size: 28px;
    color: var(--ink);
    line-height: 1.2;
    letter-spacing: 0.3px;
  }
  .holder__role {
    font-style: italic;
    font-size: 15px;
    color: var(--ink-soft);
    margin-top: 2px;
  }
  .contact {
    position: absolute;
    font-family: "Questrial", sans-serif;
    font-size: 13px;
    line-height: 16px;
    letter-spacing: 0.3px;
    color: var(--ink-soft);
  }
  .contact--online { left: 23px; top: 346px; }
  .contact--postal { right: 24px; top: 327px; text-align: right; }
</style>
</head>
<body>
<main class="canvas">
  <section class="card" aria-label="Business card front">
    <svg class="card__sweep" viewBox="0 0 708 416" aria-hidden="true">
      <defs>
        <linearGradient id="sweepFill" x1="0" y1="0" x2="1" y2="0.5">
          <stop offset="0" stop-color="var(--sweep-light)"/>
          <stop offset="1" stop-color="var(--sweep-dark)"/>
        </linearGradient>
      </defs>
      <path d="M285 0 L708 0 L708 372 C675 185 560 20 285 0 Z" fill="url(#sweepFill)"/>
    </svg>

    <div class="brand">
      <span class="brand__dot" aria-hidden="true"></span>
      <span class="brand__name">Skyvale Roster Partners Inc.</span>
    </div>

    <div class="holder">
      <div class="holder__name">Marc Delorne</div>
      <div class="holder__role">Captain</div>
    </div>

    <div class="contact contact--online">
      Skype: marc-delorne<br>
      marc.delorne@skymail.net<br>
      linkedin: Marc Delorne
    </div>

    <div class="contact contact--postal">
      58 Harbour Lane West<br>
      Ridgeford, ON, K2R4M7 Canada<br>
      +971 50 3186420 (M)<br>
      +1 905 555 0147 (H)
    </div>
  </section>
</main>
</body>
</html>
```